依頼詳細
上品なイメージで、男女共に使えるようにお願いします。
ハガキ中のどこかに、新居のパースを入れられるように場所を確保して下さい。(吹き出しや枠組みなどでサンプルを入れておいて頂ければお客様毎にこちらで差替を致します)
下の文面に加え、住所・氏名を入れる欄を作成下さい。
記載項目
転居のおしらせ

念願叶って、新築住宅が完成し転居致しました。
取り急ぎお知らせ致します。
今後とも変わらぬおつきあいを頂けますよう
よろしくお願い致します。
お近くにお越しの際にはお気軽にお立ち寄り下さい。
希望イメージ
• +5 0 +5
• シンプル
複雑
• 単色
カラフル
• 暗い
明るい
• 日常
高級
• 遊び心
厳粛
• 未来的
伝統的
• 女性的
男性的
希望する色
赤系、緑系
納品ファイル
• イラストレーター形式 (.ai)
補足説明
依頼公開後の追記内容
■ 選んだ理由

明るく、万人受けする雰囲気で、カジュアルすぎず、我が社のイメージと合っていた。
また、パースの入替もしやすかった。

■ 提案者全員のお礼・コメント

ご提案ありがとうございます。
また、今後とも様々な依頼を行っていきたいと思いますのでよろしくお願い致します。

```html
<!DOCTYPE html>
<html lang="ja">
<head>
<meta charset="utf-8">
<title>転居のおしらせ</title>
<link rel="stylesheet" href="https://fonts.googleapis.com/css2?family=Shippori+Mincho:wght@400;500&family=Cormorant+Garamond:wght@400&display=swap">
<style>
  :root {
    --paper: #ffffff;
    --card: #eeebe6;
    --ink: #4a3f36;
    --caption: #8f877f;
    --box: rgba(255,255,255,0.85);
    --photo-light: #f4f1ec;
    --photo-wood: #c9a37a;
    --leaf-light: #b9d98a;
    --leaf-dark: #5f9a3a;
  }
  * { margin: 0; padding: 0; box-sizing: border-box; }
  html, body { width: 876px; height: 1200px; overflow: hidden; background: var(--paper); }
  .postcard {
    position: relative;
    width: 876px; height: 1200px;
    background: var(--paper);
    font-family: "Shippori Mincho", serif;
    color: var(--ink);
  }
  .card-panel {
    position: absolute;
    left: 140px; top: 64px; width: 656px; height: 1090px;
    background: var(--card);
    overflow: hidden;
  }
  .house-perspective {
    position: absolute;
    left: 140px; top: 64px; width: 656px; height: 392px;
    background: linear-gradient(180deg, var(--photo-light) 0%, #ebe5dc 62%, var(--photo-wood) 100%);
  }
  .welcome-caption {
    position: absolute;
    left: 140px; top: 464px; width: 656px;
    text-align: center;
    font-family: "Cormorant Garamond", serif;
    font-size: 15px;
    letter-spacing: 2.4px;
    color: var(--caption);
  }
  .notice-title {
    position: absolute;
    left: 140px; top: 518px; width: 656px;
    text-align: center;
    font-size: 38px;
    font-weight: 500;
    letter-spacing: 4px;
    line-height: 50px;
  }
  .notice-body {
    position: absolute;
    left: 140px; top: 592px; width: 656px;
    text-align: center;
    font-size: 22px;
    line-height: 48px;
    letter-spacing: 1px;
  }
  .plant-photo {
    position: absolute;
    left: 140px; top: 842px; width: 330px; height: 312px;
    background: radial-gradient(ellipse at 45% 50%, var(--leaf-light) 0%, var(--leaf-dark) 42%, rgba(238,235,230,0) 72%);
  }
  .address-box {
    position: absolute;
    left: 455px; top: 846px; width: 326px; height: 150px;
    background: var(--box);
    border-radius: 14px;
    padding: 18px 20px 0 22px;
    font-size: 21px;
    line-height: 34px;
    font-style: normal;
  }
  .sender-name {
    position: absolute;
    left: 592px; top: 1024px; width: 190px;
    font-size: 23px;
    line-height: 38px;
  }
  .sender-name .row { display: flex; }
  .sender-name .family { width: 118px; letter-spacing: 6px; }
  .sender-name .given { letter-spacing: 6px; }
</style>
</head>
<body>
  <main class="postcard">
    <div class="card-panel"></div>
    <div class="house-perspective" role="img" aria-label="新居の内観パース（明るいリビングと階段、キッチン）"></div>
    <p class="welcome-caption">Please come and see me if you come to be my area.</p>
    <h1 class="notice-title">転居のおしらせ</h1>
    <p class="notice-body">
      念願叶って、新築住宅が完成し転居致しました。<br>
      取り急ぎお知らせ致します。<br>
      今後とも変わらぬおつきあいを頂けますよう<br>
      よろしくお願い致します。<br>
      お近くにお越しの際にはお気軽にお立ち寄り下さい。
    </p>
    <div class="plant-photo" role="img" aria-label="鉢植えの緑の観葉植物"></div>
    <address class="address-box">
      〒000-0000<br>
      ●●県●●市●●●●●<br>
      ●●●●●0-00-0
    </address>
    <div class="sender-name">
      <div class="row"><span class="family">山田</span><span class="given">太郎</span></div>
      <div class="row"><span class="family"></span><span class="given">花子</span></div>
      <div class="row"><span class="family"></span><span class="given">一郎</span></div>
    </div>
  </main>
</body>
</html>
```